ORVALO Global Commerce Inc.
Kareem Bin-Sahwan
Vice President
Unit 385, 2096 Pellmore Crescent Toronto, Ontario, Canada M4R 2K6
kareem@orvaloglobal.ca
www.orvaloglobal.ca
The company's name is "ORVALO Global Commerce Inc." The company's new logo is only stating ORVALO, i need the wording "Global Commerce Inc." to be added next to the logo at different designs for me to choose from.
The logo of the company with the wording "Global Commerce Inc." at different backgrounds and design for me to choose from.

```html
<!DOCTYPE html>
<html lang="en">
<head>
<meta charset="utf-8">
<title>ORVALO Global Commerce Inc. — Business Card</title>
<link rel="stylesheet" href="https://fonts.googleapis.com/css2?family=Montserrat:wght@500&family=Open+Sans:wght@400;600&display=swap">
<style>
  :root {
    --page-bg: #e9e7e4;
    --card-face: #f3f4f5;
    --card-shade: #e1e4e7;
    --panel-blue: #2f80c0;
    --panel-blue-dark: #2672b0;
    --swoosh-grey: #4a4f55;
    --logo-grey: #3b4046;
    --text-light: #ffffff;
  }
  * { margin: 0; padding: 0; box-sizing: border-box; }
  html, body {
    width: 1200px; height: 768px; overflow: hidden;
    background: var(--page-bg);
  }
  .business-card {
    position: absolute; left: 150px; top: 127px;
    width: 900px; height: 514px;
    box-shadow: 0 18px 40px rgba(0,0,0,0.18);
    border-radius: 4px; overflow: hidden;
  }
  .card-shapes { position: absolute; inset: 0; }
  .brand-lockup {
    position: absolute; left: 62px; top: 224px;
    display: flex; align-items: baseline; gap: 14px;
    font-family: "Montserrat", sans-serif; font-weight: 500;
    color: var(--logo-grey);
    white-space: nowrap;
  }
  .brand-name { font-size: 48px; letter-spacing: 2px; }
  .brand-tagline { font-size: 16px; letter-spacing: 0.3px; }
  .contact-block {
    position: absolute; left: 605px; top: 84px;
    color: var(--text-light);
    font-family: "Open Sans", sans-serif;
    white-space: nowrap;
  }
  .person-name { font-size: 21px; font-weight: 600; line-height: 1.2; }
  .person-role { font-size: 16px; font-weight: 400; margin-top: 2px; }
  .office-address { font-size: 14px; line-height: 1.5; margin-top: 42px; }
  .contact-list { list-style: none; margin-top: 52px; font-size: 13px; }
  .contact-list li {
    display: flex; align-items: center; gap: 10px;
    height: 23px;
  }
  .contact-list svg { width: 13px; height: 13px; flex: none; }
</style>
</head>
<body>
  <div class="business-card">
    <svg class="card-shapes" width="900" height="514" viewBox="0 0 900 514">
      <defs>
        <linearGradient id="face-fill" x1="0" y1="0" x2="1" y2="1">
          <stop offset="0" stop-color="var(--card-face)"/>
          <stop offset="1" stop-color="var(--card-shade)"/>
        </linearGradient>
        <linearGradient id="panel-fill" x1="0" y1="0" x2="0" y2="1">
          <stop offset="0" stop-color="var(--panel-blue)"/>
          <stop offset="1" stop-color="var(--panel-blue-dark)"/>
        </linearGradient>
      </defs>
      <rect class="card-face" width="900" height="514" fill="url(#face-fill)"/>
      <path class="edge-swoosh" d="M548,0 Q470,270 520,514 L566,514 Q505,260 566,0 Z" fill="var(--swoosh-grey)"/>
      <path class="info-panel" d="M566,0 Q505,260 566,514 L900,514 L900,0 Z" fill="url(#panel-fill)"/>
    </svg>

    <div class="brand-lockup">
      <span class="brand-name">ORVALO</span>
      <span class="brand-tagline">Global Commerce Inc.</span>
    </div>

    <div class="contact-block">
      <p class="person-name">Kareem Bin-Sahwan</p>
      <p class="person-role">Vice President</p>
      <p class="office-address">Unit 385, 2096 Pellmore Crescent<br>Toronto, Ontario, Canada M4R 2K6</p>
      <ul class="contact-list">
        <li>
          <svg viewBox="0 0 16 16"><path d="M3 1.5l3 3-1.6 2a9 9 0 0 0 5 5l2-1.6 3 3-2 2C6.5 14.5 1.5 9.5 1 3.5z" fill="#fff"/></svg>
          014 286 5370
        </li>
        <li>
          <svg viewBox="0 0 16 16"><rect x="4.5" y="1" width="7" height="14" rx="1.2" fill="none" stroke="#fff" stroke-width="1.6"/><circle cx="8" cy="12.5" r="0.9" fill="#fff"/></svg>
          014 286 5371
        </li>
        <li>
          <svg viewBox="0 0 16 16"><rect x="4" y="1.5" width="8" height="4" fill="#fff"/><rect x="1.5" y="6" width="13" height="6" rx="1" fill="#fff"/><rect x="4" y="10" width="8" height="4.5" fill="#fff" stroke="var(--panel-blue)" stroke-width="1"/></svg>
          014 286 5372
        </li>
        <li>
          <svg viewBox="0 0 16 16"><rect x="1.5" y="3.5" width="13" height="9" fill="none" stroke="#fff" stroke-width="1.5"/><path d="M1.5 3.5L8 9l6.5-5.5" fill="none" stroke="#fff" stroke-width="1.5"/></svg>
          kareem@orvaloglobal.ca
        </li>
        <li>
          <svg viewBox="0 0 16 16"><circle cx="8" cy="8" r="6.5" fill="none" stroke="#fff" stroke-width="1.4"/><ellipse cx="8" cy="8" rx="2.8" ry="6.5" fill="none" stroke="#fff" stroke-width="1.2"/><path d="M1.5 8h13" stroke="#fff" stroke-width="1.2"/></svg>
          www.orvaloglobal.ca
        </li>
      </ul>
    </div>
  </div>
</body>
</html>
```